Software company specialized in data analytics and professional services

We need a landing page design for our business. It should include our logo design. It should have multiple sections :
- stylish head
- what we do (data analytics software, professional services)
- contact form

Target Market(s)

Companies, B2B

Industry/Entity Type

Data

Number of Pages Required

1 page

Font styles to use
Sans Serif

Requirements
Must have
• Dark theme
Should not have
• Gradients on buttons

```html
<!DOCTYPE html>
<html lang="en">
<head>
<meta charset="UTF-8">
<title>Northgrid — Data Analytics &amp; Professional Services</title>
<link rel="stylesheet" href="https://fonts.googleapis.com/css2?family=Poppins:wght@400;500;600&display=swap">
<style>
:root{
  --bg:#0d0833;
  --band:#150d45;
  --card:#1f1560;
  --navy:#160a4c;
  --magenta:#e3189a;
  --white:#ffffff;
  --soft:#c9c5e2;
  --line:#4a4180;
  --black:#05031a;
}
*{box-sizing:border-box;margin:0;padding:0}
html,body{width:1200px;height:3600px;overflow:hidden}
body{position:relative;background:var(--bg);font-family:'Poppins',sans-serif;color:var(--white)}
.accent{color:var(--magenta)}

/* header */
.site-header{position:absolute;left:0;top:0;width:1200px;height:104px;background:var(--bg)}
.brand{position:absolute;left:112px;top:26px;font-size:48px;font-weight:600;letter-spacing:1px;color:var(--white);line-height:52px}
.main-nav{position:absolute;left:475px;top:44px;display:flex;gap:48px;font-size:18px;font-weight:500;color:var(--white)}
.main-nav .active{color:var(--magenta)}
.search-btn{position:absolute;left:1052px;top:38px;width:36px;height:36px;border-radius:50%;background:var(--magenta)}

/* hero */
.hero{position:absolute;left:0;top:104px;width:1200px;height:660px}
.hero-bg{position:absolute;inset:0}
.hero-eyebrow{position:absolute;left:108px;top:112px;font-size:28px;font-weight:500}
.hero-name{position:absolute;left:108px;top:164px;font-size:54px;font-weight:600;letter-spacing:1px}
.hero-copy{position:absolute;left:108px;top:250px;width:420px;font-size:18px;line-height:35px}
.btn{position:absolute;display:flex;align-items:center;justify-content:center;gap:12px;border-radius:30px;font-weight:500;text-transform:uppercase;border:2px solid var(--white);color:var(--white);background:transparent}
.btn-hero{left:108px;top:361px;width:220px;height:60px;font-size:20px}
.hero-illustration{position:absolute;left:530px;top:80px;width:640px;height:560px;border-radius:30px;background:linear-gradient(160deg,#e8b4f5 0%,#d86ee8 55%,#f07ad0 100%);opacity:.85}

/* about */
.section-title{position:absolute;width:1200px;left:0;text-align:center;font-size:34px;font-weight:500}
.about-copy{position:absolute;left:240px;top:852px;width:720px;text-align:center;font-size:16.5px;line-height:33px;color:var(--soft)}

/* why */
.why{position:absolute;left:0;top:1140px;width:1200px;height:652px;background:var(--band)}
.why-title{position:absolute;left:123px;top:96px;font-size:34px;font-weight:500}
.why-copy{position:absolute;left:123px;top:162px;width:470px;font-size:16px;line-height:33.5px;color:var(--soft)}
.feature{position:absolute;width:215px;background:var(--card);border-radius:6px;display:flex;flex-direction:column;align-items:center;justify-content:center;gap:22px;font-size:19px;font-weight:500;text-transform:uppercase}
.feature svg{width:70px;height:70px}

/* services */
.service-num{position:absolute;font-size:64px;font-weight:600;color:rgba(227,24,154,.28);line-height:1}
.service-title{position:absolute;font-size:26px;font-weight:500}
.service-copy{position:absolute;width:470px;font-size:15.5px;line-height:33.5px;color:var(--soft)}
.service-illustration{position:absolute;border-radius:24px}

/* contact */
.dark-base{position:absolute;left:0;top:3040px;width:1200px;height:560px}
.contact-card{position:absolute;left:112px;top:2842px;width:976px;height:474px;background:var(--card);box-shadow:0 6px 24px rgba(0,0,0,.4)}
.contact-info{position:absolute;left:0;top:0;width:410px;height:474px;background:var(--navy)}
.info-title{position:absolute;left:62px;top:44px;font-size:25px;font-weight:500}
.info-label{position:absolute;left:112px;font-size:20px;font-weight:500}
.info-value{position:absolute;left:112px;font-size:16px;line-height:36px;color:var(--soft)}
.info-icon{position:absolute;left:60px;width:22px;height:22px}
.form-title{position:absolute;left:410px;width:566px;top:52px;text-align:center;font-size:25px;font-weight:500}
.field{position:absolute;left:454px;width:470px;border-bottom:1.5px solid var(--line);font-size:12px;font-weight:500;color:var(--soft);padding-bottom:8px}
.btn-submit{left:606px;top:385px;width:170px;height:48px;font-size:16px}

/* footer */
.footer-brand{position:absolute;left:0;width:1200px;top:3386px;text-align:center;font-size:48px;font-weight:600;letter-spacing:1px}
.footer-nav{position:absolute;left:0;width:1200px;top:3470px;display:flex;justify-content:center;gap:28px;font-size:18px;font-weight:500}
.footer-nav .sep{color:#8a86a8}
.copyright{position:absolute;left:0;width:1200px;top:3530px;text-align:center;font-size:12px;font-weight:500}
</style>
</head>
<body>

<header class="site-header">
  <div class="brand">NORTHGRID</div>
  <nav class="main-nav">
    <span class="active">HOME</span><span>ABOUT US</span><span>WHAT WE DO</span><span>CONTACT US</span>
  </nav>
  <div class="search-btn">
    <svg viewBox="0 0 36 36" width="36" height="36"><circle cx="17" cy="17" r="5.5" fill="none" stroke="#fff" stroke-width="2"/><line x1="21" y1="21" x2="24" y2="24" stroke="#fff" stroke-width="2" stroke-linecap="round"/></svg>
  </div>
</header>

<section class="hero">
  <svg class="hero-bg" viewBox="0 0 1200 660" preserveAspectRatio="none">
    <defs>
      <linearGradient id="heroGrad" x1="0" y1="0" x2="0" y2="1">
        <stop offset="0" stop-color="#b750e2"/>
        <stop offset=".55" stop-color="#9a62da"/>
        <stop offset="1" stop-color="#4a94c2"/>
      </linearGradient>
    </defs>
    <path d="M0 0H1200V640C1130 680 1060 650 1030 600C1000 545 960 520 880 530C780 545 700 560 590 500C480 440 380 470 280 545C180 620 60 580 0 560Z" fill="url(#heroGrad)"/>
  </svg>
  <div class="hero-eyebrow">WELCOME TO</div>
  <div class="hero-name">NORTHGRID</div>
  <p class="hero-copy">We are a Software company specialized in data analytics and professional services.</p>
  <div class="btn btn-hero">GET STARTED <svg width="12" height="16" viewBox="0 0 12 16"><path d="M3 2l6 6-6 6" fill="none" stroke="#fff" stroke-width="2"/></svg></div>
  <div class="hero-illustration" role="img" aria-label="Isometric illustration of a team working around a large laptop with a security padlock on screen"></div>
</section>

<!-- about -->
<h2 class="section-title" style="top:785px">ABOUT <span class="accent">US</span></h2>
<p class="about-copy">Sed ut perspiciatis unde omnis iste natus error sit voluptatem accusantium doloremque laudantium, totam rem aperiam, eaque ipsa quae ab illo inventore veritatis et quasi architecto beatae vitae dicta sunt explicabo.</p>
<div class="btn" style="left:500px;top:994px;width:200px;height:56px;font-size:19px">LEARN MORE <svg width="12" height="16" viewBox="0 0 12 16"><path d="M3 2l6 6-6 6" fill="none" stroke="#fff" stroke-width="2"/></svg></div>

<!-- why -->
<section class="why">
  <h2 class="why-title">WHY <span class="accent">NORTHGRID</span></h2>
  <p class="why-copy">Sed ut perspiciatis unde omnis iste natus error sit voluptatem accusantium doloremque laudantium, totam rem aperiam, eaque ipsa quae ab illo inventore veritatis et quasi architecto beatae vitae dicta sunt explicabo.</p>
</section>

<div class="feature" style="left:609px;top:1206px;height:233px">
  <svg viewBox="0 0 70 70"><rect x="6" y="12" width="44" height="32" fill="none" stroke="#fff" stroke-width="2.5"/><path d="M14 36v-8M22 36v-12M30 36v-6" stroke="#fff" stroke-width="3"/><path d="M12 26l10-8 8 4 10-8" fill="none" stroke="#e3189a" stroke-width="2.5"/><circle cx="48" cy="44" r="9" fill="none" stroke="#e3189a" stroke-width="2.5"/><path d="M55 51l8 8" stroke="#fff" stroke-width="3"/><path d="M20 44l-4 12M36 44l4 12" stroke="#fff" stroke-width="2.5"/></svg>
  STRATEGY
</div>
<div class="feature" style="left:846px;top:1176px;height:233px">
  <svg viewBox="0 0 70 70"><rect x="6" y="6" width="18" height="18" fill="none" stroke="#fff" stroke-width="2.5"/><rect x="32" y="6" width="18" height="18" fill="none" stroke="#fff" stroke-width="2.5"/><path d="M35 15l5 5 10-13" fill="none" stroke="#e3189a" stroke-width="2.5"/><rect x="6" y="32" width="18" height="18" fill="none" stroke="#e3189a" stroke-width="2.5"/><path d="M38 62V36a4 4 0 0 1 8 0v12l10 3c4 1 5 4 4 8l-2 5" fill="none" stroke="#fff" stroke-width="2.5"/></svg>
  CHOOSE YOURS
</div>
<div class="feature" style="left:123px;top:1545px;height:210px">
  <svg viewBox="0 0 70 70"><rect x="4" y="8" width="56" height="42" rx="4" fill="none" stroke="#fff" stroke-width="2.5"/><line x1="4" y1="18" x2="60" y2="18" stroke="#fff" stroke-width="2.5"/><path d="M16 30l-5 5 5 5M30 30l5 5-5 5M25 28l-4 14" fill="none" stroke="#e3189a" stroke-width="2.5"/><circle cx="52" cy="52" r="8" fill="#1f1560" stroke="#fff" stroke-width="2.5"/><circle cx="52" cy="52" r="3" fill="none" stroke="#e3189a" stroke-width="2"/></svg>
  MANAGE DATASET
</div>
<div class="feature" style="left:363px;top:1505px;height:210px">
  <svg viewBox="0 0 70 70"><path d="M18 24v-8a10 10 0 0 1 20 0v8" fill="none" stroke="#fff" stroke-width="2.5"/><rect x="10" y="24" width="36" height="30" rx="4" fill="none" stroke="#fff" stroke-width="2.5"/><circle cx="44" cy="46" r="13" fill="#1f1560" stroke="#e3189a" stroke-width="2.5"/><circle cx="44" cy="42" r="4" fill="none" stroke="#fff" stroke-width="2.2"/><path d="M37 54a8 8 0 0 1 14 0" fill="none" stroke="#fff" stroke-width="2.2"/></svg>
  DIRECT ACCESS
</div>
<div class="feature" style="left:609px;top:1472px;height:234px">
  <svg viewBox="0 0 70 70"><circle cx="44" cy="22" r="12" fill="none" stroke="#fff" stroke-width="2.5" stroke-dasharray="5 3"/><path d="M38 22l5 5 8-9" fill="none" stroke="#e3189a" stroke-width="2.5"/><path d="M4 44h10v18H4zM14 48h12l8 4h10a3 3 0 0 1 0 6H30M14 60l14 4 30-12a3 3 0 0 0-3-5l-11 4" fill="none" stroke="#fff" stroke-width="2.5"/></svg>
  SUPPORT FRIENDLY
</div>
<div class="feature" style="left:846px;top:1436px;height:233px">
  <svg viewBox="0 0 70 70"><circle cx="35" cy="26" r="18" fill="none" stroke="#fff" stroke-width="2.5"/><circle cx="35" cy="26" r="11" fill="none" stroke="#e3189a" stroke-width="2.5"/><path d="M30 26l4 4 7-7" fill="none" stroke="#e3189a" stroke-width="2.5"/><path d="M24 40l-8 22 8-4 5 7 6-20M46 40l8 22-8-4-5 7-6-20" fill="none" stroke="#fff" stroke-width="2.5"/></svg>
  BEST QUALITY
</div>

<!-- what we do -->
<h2 class="section-title" style="top:1872px">WHAT <span class="accent">WE DO</span></h2>

<div class="service-illustration" role="img" aria-label="Isometric illustration of analysts working around a glowing data cube with charts" style="left:108px;top:1960px;width:467px;height:340px;background:linear-gradient(180deg,#3a1f7a 0%,#9b4fc8 55%,#4a2a8c 100%)"></div>
<div class="service-num" style="left:623px;top:1982px">01</div>
<h3 class="service-title" style="left:623px;top:2016px">DATA ANALYTICS SOFTWARE</h3>
<p class="service-copy" style="left:625px;top:2075px">Sed ut perspiciatis unde omnis iste natus error sit voluptatem accusantium doloremque laudantium, totam rem aperiam, eaque ipsa quae ab illo inventore veritatis et quasi architecto beatae vitae dicta sunt explicabo.</p>
<div class="btn" style="left:625px;top:2243px;width:202px;height:56px;font-size:19px">READ MORE <svg width="12" height="16" viewBox="0 0 12 16"><path d="M3 2l6 6-6 6" fill="none" stroke="#fff" stroke-width="2"/></svg></div>

<div class="service-num" style="left:493px;top:2408px">02</div>
<h3 class="service-title" style="left:108px;width:465px;text-align:right;top:2443px">PROFESSIONAL SERVICES</h3>
<p class="service-copy" style="left:103px;top:2502px;text-align:right">Sed ut perspiciatis unde omnis iste natus error sit voluptatem accusantium doloremque laudantium, totam rem aperiam, eaque ipsa quae ab illo inventore veritatis et quasi architecto beatae vitae dicta sunt explicabo.</p>
<div class="btn" style="left:371px;top:2670px;width:202px;height:56px;font-size:19px">READ MORE <svg width="12" height="16" viewBox="0 0 12 16"><path d="M3 2l6 6-6 6" fill="none" stroke="#fff" stroke-width="2"/></svg></div>
<div class="service-illustration" role="img" aria-label="Illustration of a customer and a consultant beside a large phone showing a store shelf" style="left:632px;top:2385px;width:450px;height:365px;background:linear-gradient(160deg,#3a1f7a 0%,#8a45c4 50%,#d9509f 100%)"></div>

<!-- dark base -->
<svg class="dark-base" viewBox="0 0 1200 560" preserveAspectRatio="none">
  <path d="M0 90C180 40 330 40 520 80C700 120 900 130 1080 120C1140 115 1180 100 1200 90V560H0Z" fill="var(--black)"/>
</svg>

<!-- contact -->
<section class="contact-card">
  <div class="contact-info">
    <h2 class="info-title">GET <span class="accent">IN TOUCH</span></h2>
    <svg class="info-icon" style="top:130px" viewBox="0 0 22 22"><path d="M11 1a7 7 0 0 0-7 7c0 5 7 13 7 13s7-8 7-13a7 7 0 0 0-7-7z" fill="#fff"/><circle cx="11" cy="8" r="2.6" fill="#160a4c"/></svg>
    <div class="info-label" style="top:128px">ADDRESS</div>
    <div class="info-value" style="top:168px">42, Meridian Row, Eastfield,<br>510 233.</div>
    <svg class="info-icon" style="top:276px" viewBox="0 0 22 22"><path d="M5 2l4 1 1 5-3 2a12 12 0 0 0 5 5l2-3 5 1 1 4c-1 2-3 3-5 3C9 20 2 13 2 7c0-2 1-4 3-5z" fill="#fff"/></svg>
    <div class="info-label" style="top:274px">PHONE NUMBER</div>
    <div class="info-value" style="top:312px">+1 555 014 2290</div>
    <svg class="info-icon" style="top:382px" viewBox="0 0 22 22"><rect x="1" y="4" width="20" height="14" fill="#fff"/><path d="M1 4l10 8 10-8" fill="none" stroke="#160a4c" stroke-width="1.6"/></svg>
    <div class="info-label" style="top:380px">EMAIL ADDRESS</div>
    <div class="info-value" style="top:418px">hello@northgrid.io</div>
  </div>
  <h2 class="form-title">CONTACT <span class="accent">US</span></h2>
  <div class="field" style="top:152px">FULL NAME</div>
  <div class="field" style="top:214px">EMAIL ADDRESS OR MOBILE NUMBER</div>
  <div class="field" style="top:276px;height:58px">MESSAGE..</div>
  <div class="btn btn-submit">SUBMIT NOW <svg width="10" height="14" viewBox="0 0 12 16"><path d="M3 2l6 6-6 6" fill="none" stroke="#fff" stroke-width="2"/></svg></div>
</section>

<!-- footer -->
<footer>
  <div class="footer-brand">NORTHGRID</div>
  <nav class="footer-nav">
    <span>HOME</span><span class="sep">|</span><span>ABOUT US</span><span class="sep">|</span><span>WHAT WE DO</span><span class="sep">|</span><span>CONTACT US</span>
  </nav>
  <div class="copyright">@2023 COPYRIGHTS. NORTHGRID. ALL RIGHTS RESERVED.</div>
</footer>

</body>
</html>
```